Harborwell - Direct Mail DL flyer design

Create a direct market flyer (d/l size) to compel people to act and visit our website to buy life insurance.

Copy, example images and notes are provided

Target Market(s)

Families with debt who need life insurance

Industry/Entity Type

Insurance

Requirements
Must have
• Our logo
• Colours are Blue C99, M79, Y0, K0 Green C40, M0, Y100, K0
• Copy side 1 is "For the price of a coffee you can ensure you and your family get the right start."
• Copy side 2 is "It doesn't sound like much, but when it comes to life insurance, $1 a day* can make a huge difference if you were to die.
• For the cost of a cup of coffee a day, you can ensure your family will be left with enough to protect the home, pay for ongoing living expenses and fund your children's continued education.
• Your life is important
• Apply today and get 1 month free cover
• Anchor your tomorrow
• company logo harborwell.com.au make prominant
• *For a monthly premium of $25.33, a 35 year old non-smoking male can obtain $300,000 of term life cover.
• Example for illistration purpose only. The premium cited is current as at February 2016, is based on the factors referred to in the example and subject to underwriting. You should consider whether this product is appropriate for you. Refer to the Product Disclosure Statement, available from harborwell before deciding whether to acquire the product."
• Footer
• Harborwell Pty Ltd
• ABN 47 283 916 540 AFS Licence 728194
Nice to have
• Coffee cup with pods/capsuals around it white background side 1 and coffee ring stain on reverse as watermark
• Lumaplan has been awarded - Sure Horizon - 2014 Brightpath Direct Cover Merit Prize for Term Life
• Lumaplan has been awarded - Sure Horizon - 2015 Brightpath Direct Cover Merit Prize for Term Life

```html
<!DOCTYPE html>
<html lang="en">
<head>
<meta charset="utf-8">
<title>Harborwell – For the price of a coffee</title>
<link rel="stylesheet" href="https://fonts.googleapis.com/css2?family=Roboto:wght@300;400;700;900&family=Noto+Serif:wght@400&display=swap">
<style>
  :root {
    --green-deep: #4f9a12;
    --green-mid: #6bb31d;
    --green-light: #9ad13a;
    --ring-green: #3f8a0c;
    --brand-blue: #1f3d9c;
    --award-green: #7cc21b;
    --award-text: #2f3a22;
    --white: #ffffff;
    --footer-grey: #555a60;
    --coffee-dark: #3a2416;
    --coffee-mid: #7a4e2e;
    --coffee-light: #c9a27c;
  }
  * { box-sizing: border-box; margin: 0; padding: 0; }
  html, body { width: 1200px; height: 565px; overflow: hidden; background: #ffffff; }
  .flyer {
    position: relative;
    width: 1200px;
    height: 565px;
    overflow: hidden;
    font-family: "Roboto", Arial, sans-serif;
    color: var(--white);
    background: radial-gradient(ellipse 70% 90% at 62% 40%, var(--green-light) 0%, var(--green-mid) 50%, var(--green-deep) 100%);
  }
  .hero {
    position: absolute;
    left: 100px;
    top: 162px;
    width: 520px;
    height: 520px;
    z-index: 1;
  }
  .headline {
    position: absolute;
    left: 22px;
    top: 14px;
    z-index: 2;
    font-weight: 900;
    font-size: 68px;
    line-height: 64px;
    letter-spacing: 0.5px;
    text-transform: uppercase;
    text-shadow: 0 2px 4px rgba(0,0,0,0.25);
  }
  .subline {
    position: absolute;
    left: 24px;
    top: 150px;
    z-index: 2;
    font-family: "Noto Serif", Georgia, serif;
    font-size: 23px;
    line-height: 32px;
    text-shadow: 0 1px 3px rgba(0,0,0,0.35);
  }
  .copy {
    position: absolute;
    left: 634px;
    top: 12px;
    width: 548px;
    font-weight: 300;
    font-size: 16.6px;
    line-height: 23.6px;
  }
  .awards {
    position: absolute;
    left: 623px;
    top: 421px;
    width: 441px;
    height: 82px;
    background: var(--white);
    padding: 6px 8px;
    font-size: 12.7px;
    line-height: 17.5px;
    font-weight: 400;
    color: var(--award-text);
  }
  .awards p + p { margin-top: 2px; }
  .awards .prize { color: var(--award-green); font-weight: 700; }
  .awards .product { color: var(--award-green); font-weight: 700; }
  .award-badge {
    position: absolute;
    left: 1081px;
    top: 395px;
    width: 113px;
    height: 121px;
    background: var(--white);
  }
  .logo-box {
    position: absolute;
    left: 11px;
    top: 502px;
    width: 189px;
    height: 63px;
    background: var(--white);
    z-index: 3;
    display: flex;
    align-items: center;
    gap: 8px;
    padding-left: 12px;
  }
  .logo-box .mark {
    width: 22px;
    height: 22px;
    border-radius: 50%;
    background: var(--brand-blue);
    flex: none;
  }
  .logo-box .name {
    font-weight: 700;
    font-size: 17px;
    color: var(--brand-blue);
  }
  .footer {
    position: absolute;
    left: 600px;
    top: 522px;
    width: 600px;
    height: 43px;
    background: var(--white);
    color: var(--footer-grey);
    font-size: 16.5px;
    font-weight: 400;
  }
  .footer .company { position: absolute; left: 68px; top: 11px; }
  .footer .licence { position: absolute; left: 258px; top: 11px; }
</style>
</head>
<body>
<main class="flyer">
  <svg class="hero" viewBox="0 0 520 520" role="img" aria-label="Cup of coffee on a saucer with cinnamon sticks, star anise and roasted coffee beans spilling from a hessian sack">
    <defs>
      <radialGradient id="coffeeTones" cx="45%" cy="55%" r="60%">
        <stop offset="0%" stop-color="var(--coffee-light)"/>
        <stop offset="45%" stop-color="var(--coffee-mid)"/>
        <stop offset="100%" stop-color="var(--coffee-dark)"/>
      </radialGradient>
    </defs>
    <circle cx="260" cy="260" r="258" fill="var(--ring-green)"/>
    <circle cx="260" cy="260" r="248" fill="url(#coffeeTones)"/>
  </svg>

  <h1 class="headline">For the price<br>of a coffee</h1>
  <p class="subline">you can ensure you and your<br>family get the right start.</p>

  <div class="copy">
    <p>“It doesn’t sound like much, but when it comes to life insurance, $1 a day* can make a huge difference if you were to die.</p>
    <p>- For the cost of a cup of coffee a day, you can ensure your family will be left with enough to protect the home, pay for ongoing living expenses and fund your children’s continued education.</p>
    <p>- Your life is important</p>
    <p>- Apply today and get 1 month free cover</p>
    <p>- Anchor your tomorrow</p>
    <p>- company logo harborwell.com.au make prominant</p>
    <p>- *For a monthly premium of $25.33, a 35 year old non-smoking male can obtain $300,000 of term life cover.</p>
    <p>- Example for illistration purpose only. The premium cited is current as at February 2016, is based on the factors referred to in the example and subject to underwriting. You should consider whether this product is appropriate for you. Refer to the Product Disclosure Statement, available from harborwell before deciding whether to acquire the product.”</p>
  </div>

  <div class="awards">
    <p>• <span class="product">Lumaplan</span> has been awarded - <span class="prize">Sure Horizon - 2014 Brightpath Direct Cover Merit Prize for Term Life</span></p>
    <p>• <span class="product">Lumaplan</span> has been awarded - <span class="prize">Sure Horizon - 2015 Brightpath Direct Cover Merit Prize for Term Life</span></p>
  </div>

  <div class="award-badge">
    <svg width="113" height="121" viewBox="0 0 113 121" aria-hidden="true">
      <circle cx="56" cy="50" r="37" fill="var(--brand-blue)"/>
      <rect x="11" y="92" width="91" height="19" fill="var(--brand-blue)"/>
    </svg>
  </div>

  <div class="logo-box">
    <span class="mark"></span>
    <span class="name">harborwell.com.au</span>
  </div>

  <footer class="footer">
    <span class="company">Harborwell Pty Ltd</span>
    <span class="licence">ABN 47 283 916 540 AFS Licence 728194</span>
  </footer>
</main>
</body>
</html>
```